Crumble Cove Supper Invitation

We will be having a Fish Fry on May 17th from 6PM -10PM. Location is 4721 Larkspur Ln. Mansfield, TX 76058. We need a Invitation, which includes a the header reading "Crumble Cove Supper". Wording of "Crumble Cove Supper" should incorporate both baseball and food batter. Think baseball bats dripping in batter. Admission to all you can eat fish fry will be a donation of any baseball equipment including: bats, gloves, jerseys, cleats, balls, or financial donation. Proceeds will go towards funding Pemberly Family in traveling to Dominican Republic to conduct baseball ministries. It would great to incorporate Dominican Republic flag or colors.

```html
<!DOCTYPE html>
<html lang="en">
<head>
<meta charset="utf-8">
<title>Crumble Cove Supper Invitation</title>
<link href="https://fonts.googleapis.com/css2?family=Alfa+Slab+One&family=Poppins:wght@400;500&display=swap" rel="stylesheet">
<style>
  :root{
    --backdrop:#d3d1d2;
    --navy:#1e2a5e;
    --navy-deep:#0c1640;
    --red:#e31e26;
    --red-deep:#8e1216;
    --orange:#f06a1d;
    --white:#ffffff;
  }
  *{margin:0;padding:0;box-sizing:border-box}
  html,body{width:1200px;height:1200px;overflow:hidden;background:var(--backdrop)}
  .flyer{
    position:absolute;left:264px;top:92px;width:717px;height:1015px;
    background:var(--white);overflow:hidden;
    box-shadow:0 4px 14px rgba(0,0,0,.25);
    font-family:'Poppins',sans-serif;
  }
  .flag-swoop,.bat-art,.torn-band,.night-field,.seal{position:absolute}
  .flag-swoop{left:0;top:0;width:717px;height:290px}
  .bat-art{left:242px;top:58px;width:350px;height:286px}
  .title{
    position:absolute;left:0;top:360px;width:717px;text-align:center;
    font-family:'Alfa Slab One',serif;font-size:50px;line-height:1;
    white-space:nowrap;color:var(--navy);
  }
  .title .accent{color:var(--red)}
  .date-line{
    position:absolute;left:0;top:428px;width:717px;
    display:flex;justify-content:center;align-items:center;gap:8px;
    font-size:37px;color:var(--navy);white-space:nowrap;
  }
  .rule{display:flex;flex-direction:column;gap:5px;width:84px}
  .rule span{height:3px;background:var(--orange);display:block}
  .rule.left{align-items:flex-end}
  .rule.right{align-items:flex-start}
  .address{
    position:absolute;left:146px;top:493px;height:28px;width:450px;
    background:var(--red);border-radius:14px;color:var(--white);
    font-size:22px;line-height:28px;padding-left:30px;white-space:nowrap;
  }
  .address svg{position:absolute;left:-12px;top:-3px}
  .night-field{left:0;top:640px;width:717px;height:375px;
    background:radial-gradient(ellipse at 50% 60%,#22367a 0%,var(--navy-deep) 75%)}
  .torn-band{left:0;top:535px;width:717px;height:135px}
  .donation{
    position:absolute;left:0;top:572px;width:717px;text-align:center;
    color:var(--white);font-size:19px;line-height:30px;
  }
  .seal{left:237px;top:670px;width:240px;height:240px}
  .seal-admission,.seal-to-all{position:absolute;left:237px;width:240px;text-align:center;white-space:nowrap}
  .seal-admission{top:752px;font-family:'Alfa Slab One',serif;font-size:34px;line-height:38px;color:var(--white)}
  .seal-to-all{top:797px;font-size:42px;line-height:48px;color:var(--navy)}
  .proceeds{
    position:absolute;left:0;top:928px;width:717px;text-align:center;
    color:var(--white);font-size:19px;line-height:30px;
  }
</style>
</head>
<body>
<main class="flyer">
  <svg class="flag-swoop" viewBox="0 0 717 290" role="img" aria-label="Waving Dominican Republic flag in red, white and blue">
    <defs>
      <linearGradient id="flagTone" x1="0" y1="1" x2="1" y2="0">
        <stop offset="0" stop-color="#8e1216"/>
        <stop offset=".35" stop-color="#d63a2e"/>
        <stop offset=".55" stop-color="#ececec"/>
        <stop offset=".75" stop-color="#1a2a66"/>
        <stop offset="1" stop-color="#2a3f86"/>
      </linearGradient>
    </defs>
    <polygon points="0,0 680,0 0,280" fill="url(#flagTone)"/>
  </svg>

  <svg class="bat-art" viewBox="0 0 350 286" role="img" aria-label="Baseball bat dripping orange batter into a swirling pool">
    <defs>
      <linearGradient id="batTone" x1="1" y1="0" x2="0" y2="1">
        <stop offset="0" stop-color="#1e2a5e" stop-opacity=".9"/>
        <stop offset=".6" stop-color="#3a4a86" stop-opacity=".55"/>
        <stop offset="1" stop-color="#f06a1d" stop-opacity=".6"/>
      </linearGradient>
    </defs>
    <rect x="0" y="0" width="350" height="286" rx="40" fill="url(#batTone)"/>
  </svg>

  <h1 class="title">Crumble Cove <span class="accent">Supper</span></h1>

  <p class="date-line">
    <span class="rule left"><span style="width:84px"></span><span style="width:66px"></span><span style="width:50px"></span></span>
    May 17th from 6PM -10PM
    <span class="rule right"><span style="width:84px"></span><span style="width:66px"></span><span style="width:50px"></span></span>
  </p>

  <p class="address">
    <svg width="28" height="34" viewBox="0 0 28 34" aria-hidden="true">
      <ellipse cx="14" cy="31" rx="10" ry="3" fill="#1e2a5e"/>
      <path d="M14 2a10 10 0 0 1 10 10c0 8-10 18-10 18S4 20 4 12A10 10 0 0 1 14 2z" fill="#1e2a5e" stroke="#fff" stroke-width="2"/>
      <circle cx="14" cy="12" r="4" fill="#fff"/>
    </svg>
    4721 Larkspur Ln. Mansfield, TX 76058
  </p>

  <div class="night-field"></div>

  <svg class="torn-band" viewBox="0 0 717 135" preserveAspectRatio="none" aria-hidden="true">
    <path d="M0 14 L20 9 L38 4 L55 10 L72 6 L90 12 L110 8 L128 13 L150 5 L170 10 L190 7 L212 12 L232 4 L255 9 L275 12 L298 6 L320 10 L340 7 L362 11 L385 5 L405 10 L428 8 L450 12 L470 6 L492 11 L515 7 L535 10 L558 5 L580 11 L600 8 L622 12 L645 6 L668 10 L690 7 L717 4 L717 122 L695 128 L675 123 L650 130 L628 124 L605 127 L582 122 L560 129 L540 124 L515 128 L492 122 L470 127 L448 124 L425 130 L405 123 L382 127 L360 122 L338 128 L315 124 L292 129 L270 122 L248 127 L225 123 L202 129 L180 124 L158 128 L135 122 L112 127 L90 124 L68 129 L45 123 L22 128 L0 124 Z" fill="#fff"/>
    <path d="M0 22 L22 16 L45 20 L70 14 L92 19 L118 15 L142 21 L165 16 L190 20 L215 13 L240 19 L262 16 L288 21 L312 15 L338 19 L362 14 L388 20 L412 16 L438 21 L462 14 L488 19 L512 16 L538 21 L562 15 L588 19 L612 14 L638 20 L662 16 L690 20 L717 15 L717 113 L692 118 L668 112 L645 119 L620 114 L598 117 L572 112 L548 118 L525 113 L500 117 L478 112 L452 118 L430 114 L405 119 L382 113 L358 117 L335 112 L310 118 L288 114 L262 119 L240 113 L215 117 L192 112 L168 118 L145 114 L120 119 L98 113 L72 117 L50 112 L25 118 L0 114 Z" fill="var(--red)"/>
  </svg>

  <p class="donation">You can eat fish fry will be a donation of any baseball equipment<br>including: bats, gloves, jerseys, cleats, balls, or financial donation.</p>

  <svg class="seal" viewBox="0 0 240 240" aria-hidden="true">
    <defs>
      <linearGradient id="sealTone" x1="0" y1="0" x2="1" y2="0">
        <stop offset="0" stop-color="#8e1216"/>
        <stop offset="1" stop-color="#d9262a"/>
      </linearGradient>
    </defs>
    <circle cx="120" cy="120" r="110" fill="none" stroke="var(--orange)" stroke-width="14" stroke-dasharray="6 5.5"/>
    <circle cx="120" cy="120" r="110" fill="none" stroke="url(#sealTone)" stroke-width="10" stroke-dasharray="6 5.5"/>
    <circle cx="120" cy="120" r="108" fill="url(#sealTone)"/>
    <path d="M6 125 L234 125 L228 138 L238 150 L230 162 L234 174 L6 174 L10 162 L2 150 L12 138 Z" fill="#fff" stroke="var(--orange)" stroke-width="1"/>
  </svg>
  <div class="seal-admission">Admission</div>
  <div class="seal-to-all">to all</div>

  <p class="proceeds">Proceeds will go towards funding Pemberly Family in traveling to<br>Dominican Republic to conduct baseball ministries.</p>
</main>
</body>
</html>
```